New Business Card Design Project VORASTI-Italy

we are VORASTI-Italy
our company in the market for 3 years we are luxury cosmetic company and its about time for a facelift :)
i will like to have elegant luxurious and unique business card
that will give the person that get it a unique, luxurious and elegant impression
I'm VERY OPEN FOR NEW IDEAS , even duo i add a few files of things that i see on line and i like them

i add my logo as well
my website is VORASTI.COM
(if you would like to see the main style that we have)

Target Market(s)

adult that have money :)

Industry/Entity Type

Business

Contact Information for Business Card

Name - Paul Vorasti
Position - CEO and CO Founder
address - 4817 E Larkdale
telephone - 555-384-1962
email - paul@vorasti.com
fax - 555-384-1962
website - VORASTI.COM

Colors
000000
959595
fbee3e
ffffff

Requirements
Must have
• big logo in GOLD color
• elegant look
• impressive
Nice to have
• not must but maybe classy pattern background
• not must but maybe emblem
• maybe clear plastic business card
Should not have
• colors
• images

```html
<!DOCTYPE html>
<html lang="en">
<head>
<meta charset="utf-8">
<title>VORASTI Italy – Business Card</title>
<link rel="stylesheet" href="https://fonts.googleapis.com/css2?family=Prata&display=swap">
<style>
  :root {
    --ink: #000000;
    --card-black: #050505;
    --band-light: #f7e98a;
    --band: #fbee3e;
    --gold: #d9b13b;
    --gold-text: #e6c65a;
    --paper: #ffffff;
    --stage: #e4e5e7;
    --grey: #959595;
  }
  * { box-sizing: border-box; margin: 0; padding: 0; }
  html, body { width: 1200px; height: 1200px; overflow: hidden; }
  body {
    background: var(--stage);
    font-family: "Prata", Georgia, serif;
    display: flex;
    flex-direction: column;
    align-items: center;
    justify-content: center;
    gap: 60px;
  }
  .card {
    position: relative;
    width: 900px;
    height: 514px;
    box-shadow: 0 12px 30px rgba(0,0,0,0.18);
    overflow: hidden;
  }

  /* Front */
  .card--front { background: var(--card-black); }
  .band {
    position: absolute;
    left: 0; right: 0;
    top: 48px;
    height: 170px;
    background: linear-gradient(90deg, var(--band-light), var(--band));
  }
  .front-brand {
    position: absolute;
    left: 44px;
    top: 26px;
    width: 200px;
    text-align: center;
    color: var(--ink);
  }
  .front-brand .seal {
    width: 96px; height: 96px;
    border-radius: 50%;
    background: var(--ink);
    margin: 0 auto 10px;
  }
  .front-brand .name {
    font-size: 34px;
    letter-spacing: 1px;
    line-height: 1.05;
  }
  .front-brand .name small { display: block; font-size: 12px; letter-spacing: 3px; margin-top: 4px; }

  .holder {
    position: absolute;
    right: 60px;
    top: 128px;
    text-align: left;
    color: var(--ink);
  }
  .holder__name { font-size: 36px; letter-spacing: 1px; line-height: 1; }
  .holder__title { font-size: 17px; margin-top: 8px; }

  .contacts {
    position: absolute;
    left: 250px;
    right: 60px;
    top: 300px;
    color: var(--gold-text);
    font-size: 19px;
  }
  .contacts__address { display: flex; align-items: center; gap: 10px; padding-bottom: 12px; border-bottom: 1px solid var(--gold-text); width: 260px; }
  .contacts__grid { display: flex; margin-top: 14px; padding-bottom: 14px; border-bottom: 1px solid var(--gold-text); }
  .contacts__col { display: flex; flex-direction: column; gap: 10px; padding-right: 26px; }
  .contacts__col + .contacts__col { padding-left: 26px; border-left: 1px solid var(--gold-text); }
  .row { display: flex; align-items: center; gap: 10px; }
  .icon { width: 18px; height: 18px; fill: var(--gold-text); flex: none; }

  /* Back */
  .card--back { background: var(--paper); display: flex; align-items: center; justify-content: center; }
  .back-brand { text-align: center; color: var(--gold); }
  .back-brand .seal {
    width: 120px; height: 120px;
    border-radius: 50%;
    background: var(--gold);
    margin: 0 auto 16px;
  }
  .back-brand .name { font-size: 52px; letter-spacing: 2px; line-height: 1; }
  .back-brand .name small { display: block; font-size: 16px; letter-spacing: 4px; margin-top: 8px; }
</style>
</head>
<body>

  <section class="card card--front" aria-label="Business card front">
    <div class="band"></div>
    <div class="front-brand">
      <div class="seal"></div>
      <p class="name">VORASTI<small>ITALY</small></p>
    </div>
    <div class="holder">
      <p class="holder__name">PAUL VORASTI</p>
      <p class="holder__title">CEO and CO Founder</p>
    </div>
    <div class="contacts">
      <p class="contacts__address">
        <svg class="icon" viewBox="0 0 24 24"><path d="M12 2a7 7 0 0 0-7 7c0 5 7 13 7 13s7-8 7-13a7 7 0 0 0-7-7zm0 9.5A2.5 2.5 0 1 1 12 6.5a2.5 2.5 0 0 1 0 5z"/></svg>
        4817 E Larkdale
      </p>
      <div class="contacts__grid">
        <div class="contacts__col">
          <p class="row">
            <svg class="icon" viewBox="0 0 24 24"><path d="M6.6 10.8a15 15 0 0 0 6.6 6.6l2.2-2.2a1 1 0 0 1 1-.25 11.4 11.4 0 0 0 3.6.6 1 1 0 0 1 1 1V20a1 1 0 0 1-1 1A17 17 0 0 1 3 4a1 1 0 0 1 1-1h3.5a1 1 0 0 1 1 1c0 1.25.2 2.45.6 3.6a1 1 0 0 1-.25 1z"/></svg>
            555-384-1962
          </p>
          <p class="row">
            <svg class="icon" viewBox="0 0 24 24"><path d="M6 2h9l3 3v5H6zM4 11h16a2 2 0 0 1 2 2v7H2v-7a2 2 0 0 1 2-2zm3 3v2h2v-2zm4 0v2h2v-2z"/></svg>
            555-384-1962
          </p>
        </div>
        <div class="contacts__col">
          <p class="row">
            <svg class="icon" viewBox="0 0 24 24"><path d="M12 2a10 10 0 1 0 0 20 10 10 0 0 0 0-20zm0 2c1 0 2.3 2 2.8 5H9.2C9.7 6 11 4 12 4zM4.3 11h3a17 17 0 0 0 0 2h-3a8 8 0 0 1 0-2zm4.9 4h5.6c-.5 3-1.8 5-2.8 5s-2.3-2-2.8-5zm0-2a15 15 0 0 1 0-2h5.6a15 15 0 0 1 0 2zm7.5 0a17 17 0 0 0 0-2h3a8 8 0 0 1 0 2z"/></svg>
            www.vorasti.com
          </p>
          <p class="row">
            <svg class="icon" viewBox="0 0 24 24"><path d="M2 5h20v14H2zm2 2v.5l8 5 8-5V7z"/></svg>
            paul@vorasti.com
          </p>
        </div>
      </div>
    </div>
  </section>

  <section class="card card--back" aria-label="Business card back">
    <div class="back-brand">
      <div class="seal"></div>
      <p class="name">VORASTI<small>ITALY</small></p>
    </div>
  </section>

</body>
</html>
```